project - Plume Den

Dear designers, I'm Looking for an appealing new business card design to represent us for our new e-cigarette store: The PlumE Den. Knowledgeable and friendly staff we aim for superior customer service with a positive atmosphere. Classic feel with modern touch is what we are aiming for . Lime green font and grey back round is the original color scheme but we are flexible and open to suggestions. I added some doodles to show you where my mind is at. address: 4826 97 St SW Edmonton, AB (inside the grand bazaar hall)web: theplumeden.com email: info@theplumeden.com phone : 780.555.6147 Thanks and am looking forward to seeing your creative , fresh and innovative designs.
Good luck everybody!
Gavin
lime green and charcoal grey please. thanks
Business
The PlumE Den

```html
<!DOCTYPE html>
<html lang="en">
<head>
<meta charset="utf-8">
<title>The PlumE Den — Business Card</title>
<link rel="stylesheet" href="https://fonts.googleapis.com/css2?family=Jura:wght@600&display=swap">
<style>
  :root {
    --backdrop: #26292a;
    --card-dark: #000000;
    --card-light: #ffffff;
    --title-ink: #d4d6dc;
    --ink: #2a2e30;
  }
  * { margin: 0; padding: 0; box-sizing: border-box; }
  html, body {
    width: 1200px;
    height: 1000px;
    overflow: hidden;
    background: var(--backdrop);
  }
  .stage {
    position: relative;
    width: 1200px;
    height: 1000px;
  }
  .card {
    position: absolute;
    left: 261px;
    width: 656px;
    height: 365px;
    overflow: hidden;
    box-shadow: 0 4px 14px rgba(0, 0, 0, 0.55);
  }
  .card--front {
    top: 110px;
    background: var(--card-dark);
  }
  .card--back {
    top: 503px;
    background: var(--card-light);
  }
  .brand-name {
    position: absolute;
    left: 70px;
    top: 66px;
    font-family: "Jura", sans-serif;
    font-weight: 600;
    font-size: 32px;
    line-height: 1;
    color: var(--title-ink);
    letter-spacing: 1px;
  }
  .smoke {
    position: absolute;
    left: 0;
    width: 100%;
  }
  .smoke--color {
    top: 85px;
    height: 280px;
    background:
      radial-gradient(ellipse 18% 30% at 88% 28%, rgba(240, 230, 255, 0.85), transparent 70%),
      radial-gradient(ellipse 22% 55% at 86% 55%, rgba(240, 60, 200, 0.75), transparent 70%),
      radial-gradient(ellipse 30% 45% at 58% 60%, rgba(138, 60, 240, 0.6), transparent 72%),
      radial-gradient(ellipse 40% 30% at 20% 55%, rgba(58, 60, 240, 0.7), transparent 72%),
      radial-gradient(ellipse 35% 35% at 50% 90%, rgba(58, 60, 240, 0.55), transparent 72%);
  }
  .smoke--grey {
    top: 120px;
    height: 245px;
    background:
      radial-gradient(ellipse 14% 50% at 95% 50%, rgba(40, 44, 48, 0.55), transparent 72%),
      radial-gradient(ellipse 28% 30% at 20% 75%, rgba(90, 95, 99, 0.45), transparent 72%),
      radial-gradient(ellipse 25% 35% at 55% 78%, rgba(90, 95, 99, 0.4), transparent 72%),
      radial-gradient(ellipse 20% 30% at 80% 82%, rgba(90, 95, 99, 0.3), transparent 72%);
  }
  .contact {
    position: absolute;
    left: 59px;
    top: 66px;
    list-style: none;
    font-family: "Jura", sans-serif;
    font-weight: 600;
    font-size: 15px;
    color: var(--ink);
    letter-spacing: 0.7px;
  }
  .contact li { height: 39px; white-space: nowrap; }
</style>
</head>
<body>
  <main class="stage">
    <section class="card card--front">
      <div class="smoke smoke--color" role="img" aria-label="Swirling blue, violet and pink smoke photograph"></div>
      <h1 class="brand-name">The PlumE Den</h1>
    </section>
    <section class="card card--back">
      <div class="smoke smoke--grey" role="img" aria-label="Soft grey smoke wisps photograph"></div>
      <ul class="contact">
        <li class="contact__address">4826 97 St SW Edmonton, AB (inside the grand bazaar hall)</li>
        <li class="contact__reach">email: info@theplumeden.com phone : 780.555.6147</li>
        <li class="contact__web">web: theplumeden.com</li>
      </ul>
    </section>
  </main>
</body>
</html>
```